Statement of Capabilities

We are looking for a fresh new stationary (Word Template) and a new look for our statement of capabilities....logo must be the same.

We are an electrical / lighting contractor-

www.BrightwaveUpkeep.com

Target Market(s)

B2B and government agencies

Industry/Entity Type

Electrical

Colors
eb1f27
0655a3

Requirements
Must have
• LOGO

```html
<!DOCTYPE html>
<html lang="en">
<head>
<meta charset="utf-8">
<title>Brightwave Upkeep Incorporated – Letterhead</title>
<link rel="stylesheet" href="https://fonts.googleapis.com/css2?family=Arimo:wght@400;700&display=swap">
<style>
  :root {
    --brand-red: #c4202a;
    --brand-navy: #4a5270;
    --ink: #333a55;
    --paper: #ffffff;
  }
  * { margin: 0; padding: 0; box-sizing: border-box; }
  html, body {
    width: 927px;
    height: 1200px;
    overflow: hidden;
    background: var(--paper);
  }
  .letterhead {
    position: relative;
    width: 927px;
    height: 1200px;
    background: var(--paper);
    font-family: "Arimo", Arial, sans-serif;
    overflow: hidden;
  }
  .top-band {
    position: absolute;
    left: 0; top: 0;
    width: 100%;
    height: 9px;
    background: var(--brand-navy);
  }
  .company-name {
    position: absolute;
    left: 33px;
    top: 30px;
    width: 250px;
    color: var(--brand-red);
    font-weight: 700;
    text-transform: uppercase;
    line-height: 1;
  }
  .company-name .line-main {
    display: block;
    font-size: 31px;
    letter-spacing: 0.5px;
    margin-bottom: 6px;
  }
  .company-name .line-sub {
    display: block;
    font-size: 16px;
    letter-spacing: 0.5px;
    margin-top: 4px;
    padding-left: 48px;
  }
  .contact-block {
    position: absolute;
    left: 420px;
    top: 50px;
    width: 445px;
    text-align: center;
    color: var(--ink);
    font-size: 16.5px;
    line-height: 20px;
  }
  .header-rule {
    position: absolute;
    left: 291px;
    top: 118px;
    right: 0;
    height: 4px;
    background: var(--brand-red);
  }
  .footer-shapes {
    position: absolute;
    left: 0; top: 0;
    width: 927px;
    height: 1200px;
  }
  .footer-shapes .shape-red { fill: var(--brand-red); }
  .footer-shapes .shape-navy { fill: var(--brand-navy); }
  .website {
    position: absolute;
    left: 103px;
    top: 1142px;
    color: var(--paper);
    font-size: 19px;
  }
</style>
</head>
<body>
  <div class="letterhead">
    <div class="top-band"></div>

    <div class="company-name">
      <span class="line-main">Brightwave</span>
      <span class="line-main">Upkeep</span>
      <span class="line-sub">Incorporated</span>
    </div>

    <div class="contact-block">
      <p>415 Harbor Ave Suite B, Glenmont Maryland 21044</p>
      <p>Phone 877-555-0142&nbsp; - &nbsp;Fax:&nbsp; 877-555-0143</p>
    </div>

    <div class="header-rule"></div>

    <svg class="footer-shapes" viewBox="0 0 927 1200" aria-hidden="true">
      <path class="shape-red" d="M0 1105 L484 1108 Q496 1108 500 1120 L531 1200 L0 1200 Z"/>
      <path class="shape-navy" d="M537 1134 L927 1134 L927 1200 L551 1200 L531 1144 Q529 1134 537 1134 Z"/>
    </svg>

    <p class="website">www.BrightwaveUpkeep.com</p>
  </div>
</body>
</html>
```